Detailing informational flyer

I want to design a new flyer for my automotive detailing business. The flyer should use the color scheme from the logo and be easy to read and understand the services we offer.

Font styles to use
Serif
Sans Serif

Colors
3176b5
0255a3
fbed22
33a6d7
0692cd
ffffff

Requirements
Must have
• must include all information from the copy
Nice to have
• include a Glenvaro logo such as the image attached

```html
<!DOCTYPE html>
<html lang="en">
<head>
<meta charset="utf-8">
<title>Detail Center – Ridgeview Carwash</title>
<link href="https://fonts.googleapis.com/css2?family=Ubuntu:wght@500;700&family=PT+Sans:wght@400;700&display=swap" rel="stylesheet">
<style>
  :root {
    --navy-deep: #0f2766;
    --navy: #1a3f8f;
    --icon-disc: #173a85;
    --royal: #0255a3;
    --sky: #6aa3dc;
    --sky-band: #6b9fd6;
    --yellow: #fbed22;
    --gold: #f3d84a;
    --white: #ffffff;
    --ink: #1b2f5e;
  }
  * { margin: 0; padding: 0; box-sizing: border-box; }
  html, body { width: 866px; height: 1200px; overflow: hidden; }
  body { background: var(--navy-deep); }

  .flyer {
    position: relative;
    width: 866px;
    height: 1200px;
    overflow: hidden;
    background: radial-gradient(ellipse 70% 45% at 50% 30%, #2957ae 0%, var(--navy) 45%, var(--navy-deep) 100%);
    color: var(--white);
    font-family: "PT Sans", sans-serif;
  }

  .service-strip {
    position: absolute;
    top: 50px; left: 0; right: 0;
    text-align: center;
    font-family: "Ubuntu", sans-serif;
    font-weight: 700;
    font-size: 21px;
    letter-spacing: 0.8px;
    color: var(--yellow);
    white-space: nowrap;
  }

  .hero-art {
    position: absolute;
    top: 118px; left: 177px;
    width: 512px; height: 294px;
    border-radius: 50%;
    background: radial-gradient(ellipse at 45% 50%, rgba(243,216,74,0.9) 0%, rgba(106,163,220,0.75) 45%, rgba(26,63,143,0) 72%);
  }

  .brand-title {
    position: absolute;
    top: 404px; left: 0; right: 0;
    text-align: center;
    font-family: "Ubuntu", sans-serif;
    font-weight: 700;
    font-size: 72px;
    line-height: 84px;
    letter-spacing: 1px;
    color: var(--sky);
    text-shadow: 0 4px 8px rgba(0,0,0,0.35);
    white-space: nowrap;
  }
  .brand-sub {
    position: absolute;
    top: 490px; left: 0; right: 0;
    text-align: center;
    font-family: "Ubuntu", sans-serif;
    font-weight: 700;
    font-size: 40px;
    line-height: 50px;
    letter-spacing: 9px;
    color: var(--gold);
    text-shadow: 0 3px 6px rgba(0,0,0,0.35);
    white-space: nowrap;
  }

  .service-icon {
    position: absolute;
    left: 25px;
    width: 100px; height: 100px;
  }
  .service-text {
    position: absolute;
    left: 154px;
    width: 686px;
    font-size: 17.5px;
    line-height: 18.6px;
    text-align: justify;
    hyphens: auto;
  }
  .service-text strong { color: var(--yellow); font-weight: 700; }

  .icon-exterior  { top: 579px; }
  .icon-interior  { top: 696px; }
  .icon-mini      { top: 815px; }
  .icon-headlight { top: 934px; }
  .text-exterior  { top: 595px; }
  .text-interior  { top: 696px; }
  .text-mini      { top: 811px; }
  .text-headlight { top: 962px; }

  .cta {
    position: absolute;
    top: 1057px; left: 23px;
    font-weight: 700;
    font-size: 17.5px;
    line-height: 20px;
    color: var(--yellow);
    white-space: nowrap;
  }
  .partner {
    position: absolute;
    top: 1052px; left: 676px;
    display: flex; align-items: center; gap: 8px;
    font-family: "PT Sans", sans-serif;
    font-weight: 700;
    font-size: 26px;
    line-height: 32px;
    color: var(--yellow);
  }
  .partner-dot { width: 18px; height: 18px; border-radius: 50%; background: var(--yellow); }

  .address-band {
    position: absolute;
    left: 0; right: 0; bottom: 0;
    height: 70px;
    background: var(--sky-band);
    display: flex; align-items: flex-end; justify-content: center;
    padding-bottom: 10px;
    font-family: "Ubuntu", sans-serif;
    font-weight: 700;
    font-size: 21px;
    letter-spacing: 1px;
    color: var(--ink);
  }
  .phone-pill {
    position: absolute;
    top: 1097px; left: 251px;
    width: 368px; height: 48px;
    border-radius: 18px;
    background: var(--gold);
    display: flex; align-items: center; justify-content: center; gap: 14px;
    font-family: "Ubuntu", sans-serif;
    font-weight: 700;
    font-size: 28px;
    color: var(--royal);
  }
</style>
</head>
<body>
<main class="flyer">
  <p class="service-strip">CAR WASH · OIL LUBE &amp; FILTER SERVICE · AUTO DETAILING SERVICE</p>

  <div class="hero-art" role="img" aria-label="Illustration of a yellow convertible sports car with light blue soap bubbles behind it"></div>

  <h1 class="brand-title">DETAIL CENTER</h1>
  <p class="brand-sub">RIDGEVIEW CARWASH</p>

  <svg class="service-icon icon-exterior" viewBox="0 0 100 100" role="img" aria-label="Car wash icon">
    <circle cx="50" cy="50" r="46" fill="#173a85"/>
    <path d="M4 55 A46 46 0 0 0 96 55" fill="none" stroke="#f3d84a" stroke-width="2.5"/>
    <circle cx="50" cy="46" r="18" fill="#f3d84a"/>
  </svg>
  <p class="service-text text-exterior"><strong>EXTERIOR DETAILING INCLUDES:</strong> We wash, clay, compound, polish, and wax, as needed to restore the deep rich gloss and provide a durable shine for that “new car” look. This process removes light oxidation from the vehicle and protects the clear coat finish. Finishing touches include rim cleaning and tire shine.</p>

  <svg class="service-icon icon-interior" viewBox="0 0 100 100" role="img" aria-label="Seat cleaning icon">
    <circle cx="50" cy="50" r="46" fill="#173a85"/>
    <path d="M4 55 A46 46 0 0 0 96 55" fill="none" stroke="#f3d84a" stroke-width="2.5"/>
    <circle cx="50" cy="46" r="18" fill="#f3d84a"/>
  </svg>
  <p class="service-text text-interior"><strong>INTERIOR DETAILING SHAMPOO INCLUDES:</strong> We perform a deep cleaning of the interior such as the dashboard, door jams, center console, trunk area, upholstered seats, andall carpets and mats. This process will remove soils and most stains. Windows are cleaned inside and out. All leather is dressed to provide a protective finish. Air fresher is available upon request.</p>

  <svg class="service-icon icon-mini" viewBox="0 0 100 100" role="img" aria-label="Wheel cleaning icon">
    <circle cx="50" cy="50" r="46" fill="#173a85"/>
    <path d="M4 55 A46 46 0 0 0 96 55" fill="none" stroke="#f3d84a" stroke-width="2.5"/>
    <circle cx="50" cy="46" r="18" fill="#f3d84a"/>
  </svg>
  <p class="service-text text-mini"><strong>MINI DETAIL/ VIP SERVICE INCLUDES:</strong> Ridgeview Special Wash with triple polish wax, Glenvaro Shield protectant, tire shine, and a detailed and gentle cleaning of the upholstery. 4 rubber or carpet mats are shampooed. All interior surfaces are dressed including dashboard, door panels, center console. This is followed by a detailed carpet and upholstery vacuum with compressed air to remove dirt from hard to reach places. For added shine ask about adding on our express wax service to your mini detail package.</p>

  <svg class="service-icon icon-headlight" viewBox="0 0 100 100" role="img" aria-label="Headlight polishing icon">
    <circle cx="50" cy="50" r="46" fill="#173a85"/>
    <path d="M4 55 A46 46 0 0 0 96 55" fill="none" stroke="#f3d84a" stroke-width="2.5"/>
    <circle cx="50" cy="46" r="18" fill="#f3d84a"/>
  </svg>
  <p class="service-text text-headlight"><strong>HEADLIGHT RESTORATION:</strong> This shop proudly offers the Headlight Service, which can polish or restore your headlight to a clear, safe condition at a fraction of the cost of headlight replacement! Restore the lens to a clear, shiny &amp; safe condition.</p>

  <p class="cta">Ask to speak to a manager about scheduling any of our detailing services.</p>

  <div class="partner"><span class="partner-dot"></span>GLENVARO</div>

  <footer class="address-band">48-20 Larchmont Ave Maple Hollow 10950</footer>

  <div class="phone-pill">
    <svg width="30" height="30" viewBox="0 0 30 30" aria-hidden="true">
      <circle cx="15" cy="15" r="13" fill="none" stroke="#0255a3" stroke-width="2.5"/>
      <path d="M10 8.5c1-.6 1.8-.2 2.3.8l.9 1.8c.3.7.1 1.3-.5 1.8l-.8.6c.7 1.6 1.9 2.9 3.5 3.7l.6-.8c.5-.6 1.1-.8 1.8-.5l1.8.9c1 .5 1.3 1.4.7 2.3-.8 1.3-2.2 1.8-3.6 1.3-3.6-1.3-6.4-4.1-7.6-7.7-.5-1.5 0-2.9 1-4z" fill="#0255a3"/>
    </svg>
    <span>+1 555-014-7720</span>
  </div>
</main>
</body>
</html>
```